Regenerative Medicine Brochure

I want a clean modern bi-fold or tri-fold brochure. We offer non-surgical joint repair for knees, shoulders, and hips. We have many services available including regenerative medicine including stem cell allograft, palatelet rich plasma, prolotherapy, triggerpoint injection, chiropractic and rehab therapies. We are a modern multidisciplinary clinic in coastal California. My logo is already complete and is a vibrant green color. I prefer lots of white space with some areas for service description and what conditions may benefit from the services. Design should convey modern treatments, upscale office and practice, and our target audience is older adults who want to maintain an active pain-free lifestyle.

Target Market(s)

Sports injuries, athletes, seniors who are active, knee pain, shoulder pain, arthritis.

Industry/Entity Type

Alternative Medicine

Font styles to use
Serif

Colors
9bcb3c

Requirements
Must have
• Small white space where we can write date, time, location of next event/class. Colors in brochure to coordinate with logo colors provided.

```html
<!DOCTYPE html>
<html lang="en">
<head>
<meta charset="utf-8">
<title>Greenhaven – Regenerative Medicine Brochure</title>
<link rel="stylesheet" href="https://fonts.googleapis.com/css2?family=Playfair+Display:wght@700&family=Lora:ital,wght@0,400;0,600;1,400&display=swap">
<style>
  :root {
    --green: #7ed957;
    --paper: #fafafa;
    --ink: #1f1f1f;
    --white: #ffffff;
    --rule: #cfe9c2;
  }
  * { box-sizing: border-box; margin: 0; padding: 0; }
  html, body { width: 1200px; height: 927px; overflow: hidden; background: var(--paper); }
  .brochure {
    position: relative; width: 1200px; height: 927px; overflow: hidden;
    background: var(--paper); font-family: "Lora", serif; color: var(--ink);
  }
  .services {
    position: absolute; left: 0; top: 0; width: 398px; height: 557px;
    text-align: center; padding-top: 48px;
  }
  .services__title {
    font-family: "Playfair Display", serif; color: var(--green);
    font-size: 42px; font-weight: 700; line-height: 1; margin-bottom: 38px;
  }
  .service { margin-bottom: 36px; }
  .service__name {
    color: var(--green); font-size: 14px; font-weight: 600; letter-spacing: 3px;
    line-height: 1; margin-bottom: 14px;
  }
  .service__text { font-size: 12.5px; line-height: 20.5px; padding: 0 44px; }
  .photo { position: absolute; }
  .photo--therapy {
    left: 398px; top: 0; width: 403px; height: 557px;
    background: linear-gradient(135deg, #f2f4f6 0%, #dfe3e8 45%, #c9b2a2 60%, #3f5f8e 85%, #e9ecef 100%);
  }
  .photo--doctor {
    left: 801px; top: 301px; width: 399px; height: 626px;
    background: linear-gradient(160deg, #cfd9e2 0%, #b9c7d3 40%, #e8e4e0 65%, #f4f6f8 100%);
  }
  .band { position: absolute; left: 0; top: 557px; width: 801px; height: 20px; background: var(--green); }
  .headline {
    position: absolute; left: 801px; top: 0; width: 399px; height: 301px;
    display: flex; align-items: center; justify-content: center; padding-bottom: 14px;
    font-family: "Playfair Display", serif; color: var(--green);
    font-size: 64px; font-weight: 700; line-height: 72px; text-align: center;
  }
  .tagline {
    position: absolute; left: 835px; top: 751px; width: 365px; height: 123px;
    background: var(--green); color: var(--white);
    display: flex; align-items: center; justify-content: center; text-align: center;
    font-size: 22px; font-weight: 600; line-height: 30px; letter-spacing: 1px;
  }
  .event {
    position: absolute; left: 40px; top: 662px; width: 324px; text-align: center;
    color: var(--green); font-size: 19px; font-style: italic;
    letter-spacing: 3px; line-height: 43px;
  }
  .event__field { display: flex; justify-content: center; align-items: baseline; gap: 8px; }
  .event__blank { display: inline-block; width: 140px; border-bottom: 1px solid var(--rule); }
  .contact { position: absolute; left: 440px; top: 634px; width: 320px; text-align: center; }
  .brand {
    display: flex; align-items: center; justify-content: center; gap: 10px; height: 76px;
    font-family: "Playfair Display", serif; color: var(--green); font-size: 32px; font-weight: 700;
  }
  .brand__mark { width: 18px; height: 18px; background: var(--green); }
  .contact__title {
    font-family: "Playfair Display", serif; color: var(--green);
    font-size: 38px; font-weight: 700; line-height: 1; margin: 22px 0 20px;
  }
  .contact__line { font-size: 12.5px; line-height: 20.5px; }
</style>
</head>
<body>
<main class="brochure">
  <section class="services">
    <h2 class="services__title">SERVICES</h2>
    <div class="service">
      <h3 class="service__name">STEM CELL ALLOGRAFT</h3>
      <p class="service__text">Non-surgical joint repair for knees, shoulders and hips. Helps ease arthritis pain and supports natural healing.</p>
    </div>
    <div class="service">
      <h3 class="service__name">PLATELET-RICH PLASMA</h3>
      <p class="service__text">Your own platelets speed recovery from sports injuries, tendon strain and joint wear, with no downtime.</p>
    </div>
    <div class="service">
      <h3 class="service__name">PROLOTHERAPY</h3>
      <p class="service__text">Injections that strengthen loose ligaments, paired with trigger point, chiropractic and rehab therapies.</p>
    </div>
  </section>

  <div class="photo photo--therapy" role="img" aria-label="Therapist treating the ankle of a seated athlete on a treatment bench"></div>
  <div class="band"></div>

  <h1 class="headline">CLINIC<br>NOW<br>OPEN!</h1>
  <div class="photo photo--doctor" role="img" aria-label="Smiling senior doctor in a white coat with a stethoscope"></div>
  <p class="tagline">Serving the<br>neighborhood.</p>

  <section class="event" aria-label="Next event details">
    <p>NEXT CLASS</p>
    <p class="event__field">DATE <span class="event__blank"></span></p>
    <p class="event__field">TIME <span class="event__blank"></span></p>
    <p class="event__field">PLACE <span class="event__blank"></span></p>
  </section>

  <section class="contact">
    <div class="brand"><span class="brand__mark"></span>Greenhaven</div>
    <h2 class="contact__title">CONTACT US</h2>
    <p class="contact__line">48 Tidewater Lane, Seacliff, CA 93001</p>
    <p class="contact__line">+1 (805) 555-0142</p>
    <p class="contact__line">hello@greenhavenclinic.com</p>
    <p class="contact__line">www.greenhavenclinic.com</p>
  </section>
</main>
</body>
</html>
```